Business Card for Dental Office

Our office is in the Hillcrest section of San Diego, California which is a well-established area. Maybe the back can be a map of our office location

```html
<!DOCTYPE html>
<html lang="en">
<head>
<meta charset="utf-8">
<title>Canyon Row Dental – Business Card</title>
<link href="https://fonts.googleapis.com/css2?family=Open+Sans:wght@400;600;700&display=swap" rel="stylesheet">
<style>
  :root {
    --backdrop: #2a2a2a;
    --card: #1b1b1b;
    --card-edge: #262626;
    --ink-bright: #ffffff;
    --ink-soft: #d8d8d8;
    --ink-muted: #8f8f8f;
    --ink-gloss: #9a9a9a;
  }
  * { margin: 0; padding: 0; box-sizing: border-box; }
  html, body {
    width: 1200px;
    height: 1000px;
    overflow: hidden;
    background: var(--backdrop);
    font-family: "Open Sans", sans-serif;
  }
  .canvas {
    position: relative;
    width: 1200px;
    height: 1000px;
  }
  .card {
    position: absolute;
    left: 250px;
    width: 700px;
    height: 400px;
    background: var(--card);
    border: 1px solid var(--card-edge);
    box-shadow: 0 18px 40px rgba(0,0,0,0.45);
  }
  .card--front { top: 60px; }
  .card--back  { top: 540px; }

  /* Front */
  .brand {
    position: absolute;
    top: 50%;
    left: 50%;
    transform: translate(-50%, -50%);
    display: flex;
    align-items: center;
    gap: 14px;
  }
  .brand__dot {
    width: 22px;
    height: 22px;
    border-radius: 50%;
    background: var(--ink-gloss);
  }
  .brand__name {
    font-weight: 600;
    font-size: 30px;
    letter-spacing: 1px;
    color: var(--ink-gloss);
  }

  /* Back */
  .identity {
    position: absolute;
    top: 104px;
    right: 408px;
    text-align: right;
  }
  .identity__name {
    font-weight: 700;
    font-size: 30px;
    letter-spacing: 0.5px;
    color: var(--ink-bright);
    line-height: 1.2;
  }
  .identity__role {
    font-weight: 600;
    font-size: 20px;
    color: var(--ink-muted);
    margin-top: 2px;
  }
  .divider {
    position: absolute;
    top: 112px;
    left: 312px;
    width: 2px;
    height: 66px;
    background: var(--ink-soft);
  }
  .contacts {
    position: absolute;
    top: 110px;
    left: 332px;
    list-style: none;
  }
  .contacts__item {
    display: flex;
    align-items: center;
    gap: 14px;
    font-size: 17px;
    color: var(--ink-soft);
    height: 23px;
  }
  .contacts__item svg { width: 14px; height: 14px; fill: var(--ink-muted); }
  .address {
    position: absolute;
    left: 70px;
    bottom: 92px;
    display: flex;
    align-items: center;
    gap: 12px;
    font-size: 18px;
    color: var(--ink-soft);
    letter-spacing: 0.5px;
  }
  .address svg { width: 16px; height: 20px; fill: var(--ink-muted); }
</style>
</head>
<body>
<main class="canvas">
  <section class="card card--front">
    <div class="brand">
      <span class="brand__dot"></span>
      <span class="brand__name">Canyon Row Dental</span>
    </div>
  </section>

  <section class="card card--back">
    <div class="identity">
      <p class="identity__name">DANIEL REYES</p>
      <p class="identity__role">Founer/CEO</p>
    </div>
    <span class="divider"></span>
    <ul class="contacts">
      <li class="contacts__item">
        <svg viewBox="0 0 16 16" aria-hidden="true"><path d="M3.6 1.5l2.3 2.4-1.4 1.8c.9 2 2.6 3.7 4.6 4.6l1.8-1.4 2.4 2.3-1.4 2.3C6.8 13.4 2.6 9.2 1.3 3l2.3-1.5z"/></svg>
        <span>+1 619 555 0142</span>
      </li>
      <li class="contacts__item">
        <svg viewBox="0 0 16 16" aria-hidden="true"><path d="M1 3h14v2L8 9 1 5z M1 6.5l7 4 7-4V13H1z"/></svg>
        <span>hello@canyonrow.com</span>
      </li>
      <li class="contacts__item">
        <svg viewBox="0 0 16 16" aria-hidden="true"><path d="M9.5 1a5.5 5.5 0 1 1-3.6 9.7L2.4 14.2 1.3 13.1l3.5-3.5A5.5 5.5 0 0 1 9.5 1zm0 2a3.5 3.5 0 1 0 0 7 3.5 3.5 0 0 0 0-7z"/></svg>
        <span>www.canyonrow.com</span>
      </li>
    </ul>
    <p class="address">
      <svg viewBox="0 0 16 20" aria-hidden="true"><path d="M8 0a7 7 0 0 1 7 7c0 5-7 13-7 13S1 12 1 7a7 7 0 0 1 7-7zm0 4a3 3 0 1 0 0 6 3 3 0 0 0 0-6z"/></svg>
      <span>1420 Garnet Lane, San Diego, California</span>
    </p>
  </section>
</main>
</body>
</html>
```